Soccer (Football) travel website

I need a responsive 1-page website design for a vacation/trip review website, plus a basic logo. The site's name is GlobalPitchJourneys.com.

A site I have in mind is HarborVerdict.com:

https://www.harborverdict.example/sailto/sailroutes.cfm?port=149&startDate=2019-08

Target Market(s)

Landing page used to attract people after they've clicked on an advertisement

Industry/Entity Type

Travel

Logo Text

GlobalPitchJourneys.com

Number of Pages Required

1 page

Font styles to use
Sans Serif

Colors

Designer to choose colors to be used in the design.

Requirements
Must have
• A header that takes up very little vertical space.
• I've attached one file. This is what the content will consist of in the center of the site: a photo of a stadium with some description text below it.
Nice to have
• Needs to have a simple nav plus links for social media and newsletter

```html
<!DOCTYPE html>
<html lang="en">
<head>
<meta charset="utf-8">
<title>GlobalPitchJourneys</title>
<link href="https://fonts.googleapis.com/css2?family=Oswald:wght@400;500&family=Montserrat:wght@400;500;600;700&display=swap" rel="stylesheet">
<style>
:root{
  --orange:#f15a22;
  --ink:#222;
  --body:#555;
  --muted:#888;
  --line:#1f3a6e;
  --band:#ececec;
  --footer:#333;
  --footer-base:#232323;
  --white:#fff;
}
*{box-sizing:border-box;margin:0;padding:0}
html,body{width:847px;height:1200px;overflow:hidden;background:var(--white)}
body{position:relative;font-family:"Montserrat",sans-serif;color:var(--ink)}
.abs{position:absolute}
.heading{font-family:"Oswald",sans-serif;font-weight:500;font-size:16px;text-decoration:underline;text-underline-offset:3px;text-decoration-thickness:1px;color:var(--ink)}

/* header */
.site-header{position:absolute;left:0;top:0;width:847px;height:48px;background:var(--white)}
.brand{position:absolute;left:114px;top:13px;font-family:"Oswald",sans-serif;font-weight:500;font-size:14px;color:var(--orange);letter-spacing:-.2px;white-space:nowrap}
.main-nav{position:absolute;left:246px;top:20px;font-size:7px;font-weight:600;display:flex;gap:10px;white-space:nowrap}
.main-nav .caret{font-size:5.5px;margin-left:3px}
.search{position:absolute;left:352px;top:12px;width:168px;height:25px;border:1px solid #999;font-size:7.5px;color:var(--muted);display:flex;align-items:center;padding-left:10px;gap:7px}
.tools{position:absolute;left:528px;top:12px;display:flex;gap:12px}
.tool{display:flex;flex-direction:column;align-items:center;font-size:7px;color:var(--muted);gap:2px}
.social-dot{position:absolute;top:17px;width:15px;height:15px;border-radius:50%;background:#111}

/* hero */
.hero{position:absolute;left:0;top:48px;width:847px;height:118px;background:linear-gradient(180deg,#6f89a8 0%,#8ea4bd 40%,#c1ccd8 70%,#7d8fa4 100%)}
.hero-title{position:absolute;left:0;width:847px;top:38px;text-align:center;font-family:"Oswald",sans-serif;font-weight:500;font-size:15px;color:var(--white);text-decoration:underline;text-underline-offset:3px;letter-spacing:.5px}
.hero-sub{position:absolute;left:0;width:847px;top:65px;text-align:center;font-size:9.5px;font-weight:500;color:var(--white);letter-spacing:.3px}

/* tours */
.tour{position:absolute;top:253px;width:198px}
.tour-photo{width:198px;height:139px}
.tour-title{margin-top:14px;font-family:"Oswald",sans-serif;font-weight:500;font-size:10.5px}
.tour-text{margin-top:6px;font-size:7.6px;line-height:14px;color:var(--body)}
.learn{display:inline-flex;align-items:center;gap:4px;margin-top:4px;font-size:6.3px;font-weight:700;padding-bottom:4px;border-bottom:1.5px solid var(--line)}
.circ{display:inline-block;width:9px;height:9px;border:1px solid #999;border-radius:50%;font-size:5px;line-height:7px;text-align:center;color:#777;font-weight:400}

/* reviews */
.reviews{position:absolute;left:2px;top:553px;width:845px;height:298px;background:var(--band);overflow:hidden}
.reviews .stripe{position:absolute;top:0;width:60px;height:298px;background:rgba(255,255,255,.35);transform:skewX(-14deg)}
.review-card{position:absolute;top:625px;width:302px;height:171px;background:#e9e9e9;box-shadow:0 1px 4px rgba(0,0,0,.25)}
.review-photo{position:absolute;left:8px;top:6px;width:127px;height:159px}
.view-details{position:absolute;left:0;width:127px;bottom:30px;text-align:center;font-size:7.5px;color:var(--white);text-decoration:underline;font-weight:500}
.review-title{position:absolute;left:146px;top:22px;font-size:9.5px;font-weight:600;white-space:nowrap}
.stars{position:absolute;left:146px;top:42px;display:flex;align-items:center;gap:1px;font-size:7px;font-weight:600}
.stars span{margin-left:7px}
.facts{position:absolute;left:146px;top:67px;width:142px;height:58px;background:#f4f4f4;padding:6px 12px;font-size:7.4px;line-height:15.5px;white-space:nowrap}
.facts b{font-weight:600}
.note{position:absolute;left:146px;top:133px;width:142px;font-size:7.6px;line-height:11.5px}
.review-links{position:absolute;top:809px;display:flex;font-size:6.2px;font-weight:700;white-space:nowrap}
.review-links a{color:var(--ink);text-decoration:none;display:inline-flex;gap:3px;align-items:center;padding-bottom:4px;border-bottom:1.5px solid var(--line);margin-right:14px}
.pager{position:absolute;left:724px;top:587px;display:flex;gap:3px}

/* newsletter */
.subline{position:absolute;left:114px;top:918px;font-size:8.5px;color:var(--body)}
.email{position:absolute;left:114px;top:948px;width:468px;height:29px;border:1px solid #999;font-size:7.8px;padding-left:15px;display:flex;align-items:center}
.send{position:absolute;left:589px;top:948px;width:144px;height:29px;background:var(--orange);color:var(--white);font-size:9.5px;font-weight:700;display:flex;align-items:center;justify-content:center;gap:8px}

/* footer */
.site-footer{position:absolute;left:0;top:1020px;width:847px;height:158px;background:var(--footer);color:#aaa}
.foot-brand{position:absolute;left:90px;width:200px;top:30px;text-align:center;font-family:"Oswald",sans-serif;font-weight:500;font-size:19px;color:var(--orange)}
.copy{position:absolute;left:90px;width:200px;top:68px;text-align:center;font-size:7.5px;line-height:14.5px;color:#999}
.flag{position:absolute;top:108px;width:20px;height:20px}
.col-title{position:absolute;top:37px;font-size:9px;font-weight:600;color:var(--white);letter-spacing:.3px}
.col-list{position:absolute;top:62px;list-style:none;font-size:7.6px;line-height:16px;color:#999}
.col-list li::before{content:"";display:inline-block;width:3px;height:3px;background:#777;margin-right:8px;vertical-align:middle}
.base{position:absolute;left:0;top:1178px;width:847px;height:22px;background:var(--footer-base);font-size:7.5px;color:#999}
</style>
</head>
<body>

<header class="site-header">
  <div class="brand">GlobalPitchJourneys</div>
  <nav class="main-nav"><span>Reaserch<span class="caret">▼</span></span><span>Find a Cruise</span></nav>
  <div class="search">
    <svg width="10" height="10" viewBox="0 0 10 10"><circle cx="4" cy="4" r="3" fill="none" stroke="#222" stroke-width="1.4"/><line x1="6.2" y1="6.2" x2="9.3" y2="9.3" stroke="#222" stroke-width="1.4"/></svg>
    Search Keyword
  </div>
  <div class="tools">
    <div class="tool"><svg width="11" height="11" viewBox="0 0 11 11"><path d="M2 9 L2.5 7 L8 1.5 L9.5 3 L4 8.5 Z" fill="#777"/></svg>Write Review</div>
    <div class="tool"><svg width="13" height="11" viewBox="0 0 13 11"><ellipse cx="5" cy="4" rx="5" ry="3.6" fill="#777"/><ellipse cx="8.5" cy="6.5" rx="4.3" ry="3.2" fill="#999"/></svg>Boards</div>
    <div class="tool"><svg width="11" height="11" viewBox="0 0 11 11"><circle cx="5.5" cy="3" r="2.6" fill="#777"/><path d="M0.5 11 Q5.5 3.5 10.5 11 Z" fill="#777"/></svg>Login</div>
    <div class="tool"><svg width="11" height="11" viewBox="0 0 11 11"><circle cx="5.5" cy="5.5" r="5.2" fill="#777"/><path d="M3 5.6 L4.9 7.4 L8 3.9" fill="none" stroke="#fff" stroke-width="1.3"/></svg>Saved</div>
  </div>
  <span class="social-dot" style="left:695px"></span>
  <span class="social-dot" style="left:716px"></span>
</header>

<section class="hero" role="img" aria-label="Cruise ship bow under a cloudy blue sky">
  <h1 class="hero-title">WELCOME TO GLOBALPITCHJOURNEYS</h1>
  <p class="hero-sub">Lorem Ipsum is simply dummy text of the printing and typesetting industry.</p>
</section>

<h2 class="heading abs" style="left:106px;top:211px">Featured Tours</h2>

<article class="tour" style="left:106px">
  <div class="tour-photo" role="img" aria-label="Stadium with red stands and sunlit pitch" style="background:linear-gradient(180deg,#d8d8d4 0%,#c9cac6 35%,#a42a2a 50%,#b93a35 58%,#5c8a3a 70%,#d2a236 100%)"></div>
  <h3 class="tour-title">MANCHESTER, NOVEMBER</h3>
  <p class="tour-text">Lorem Ipsum is simply dummy text of the printing and typesetting industry. Lorem Ipsum has been the industry's standard specimen book</p>
  <span class="learn">LEARN MORE <span class="circ">↓</span></span>
</article>
<article class="tour" style="left:317px">
  <div class="tour-photo" role="img" aria-label="Stadium arch lit up at night" style="background:linear-gradient(180deg,#0c0c0e 0%,#1a1a1e 45%,#8a7a40 62%,#3c3e44 75%,#6d737c 100%)"></div>
  <h3 class="tour-title">LONDON, DECEMBER</h3>
  <p class="tour-text">Lorem Ipsum is simply dummy text of the printing and typesetting industry. Lorem Ipsum has been the industry's standard specimen book</p>
  <span class="learn">LEARN MORE <span class="circ">↓</span></span>
</article>
<article class="tour" style="left:527px">
  <div class="tour-photo" role="img" aria-label="Empty red stadium seats above a green pitch" style="background:linear-gradient(180deg,#2b2b2f 0%,#b3262c 18%,#c8303a 55%,#4e7f3a 68%,#3f7232 100%)"></div>
  <h3 class="tour-title">LIVERPOOL, MARCH</h3>
  <p class="tour-text">Lorem Ipsum is simply dummy text of the printing and typesetting industry. Lorem Ipsum has been the industry's standard specimen book</p>
  <span class="learn">LEARN MORE <span class="circ">↓</span></span>
</article>

<section class="reviews" aria-label="Latest reviews">
  <span class="stripe" style="left:120px"></span>
  <span class="stripe" style="left:330px"></span>
  <span class="stripe" style="left:720px"></span>
</section>
<h2 class="heading abs" style="left:126px;top:586px">Latest Reviews</h2>
<div class="pager">
  <svg width="10" height="12" viewBox="0 0 10 12"><path d="M7 1 L2 6 L7 11" fill="none" stroke="#333" stroke-width="1.5"/></svg>
  <svg width="10" height="12" viewBox="0 0 10 12"><path d="M3 1 L8 6 L3 11" fill="none" stroke="#333" stroke-width="1.5"/></svg>
</div>

<article class="review-card" style="left:126px">
  <div class="review-photo" role="img" aria-label="Traveller in front of a cruise ship" style="background:linear-gradient(160deg,#5d7fa3 0%,#9fb3c8 45%,#8a6b55 75%,#5a6a7a 100%)"><span class="view-details">View Details</span></div>
  <h3 class="review-title">7-day Western Mediterranean</h3>
  <div class="stars">
    <svg width="60" height="10" viewBox="0 0 60 10"><g fill="#e2501f"><path id="s" d="M5 0.5 L6.3 3.6 L9.6 3.8 L7 5.9 L7.9 9.2 L5 7.4 L2.1 9.2 L3 5.9 L0.4 3.8 L3.7 3.6 Z"/><use href="#s" x="12"/><use href="#s" x="24"/><use href="#s" x="36"/></g><use href="#s" x="48" fill="#777"/></svg>
    <span>4,603 Reviews</span>
  </div>
  <div class="facts"><b>Departs</b> : Barcelona<br><b>Ports</b> : Barcelona Naples Rome<br><b>Dates</b> : Aug 4, Aug11, Aug 18</div>
  <p class="note">We currently have no partners with this itinerary available</p>
</article>
<article class="review-card" style="left:443px">
  <div class="review-photo" role="img" aria-label="Cruise ship balconies over blue water" style="background:linear-gradient(160deg,#2c5a46 0%,#6f8fa2 40%,#c4d0d8 60%,#2f5f82 100%)"><span class="view-details">View Details</span></div>
  <h3 class="review-title">7-day Western Mediterranean</h3>
  <div class="stars">
    <svg width="60" height="10" viewBox="0 0 60 10"><g fill="#e2501f"><use href="#s"/><use href="#s" x="12"/><use href="#s" x="24"/><use href="#s" x="36"/></g><use href="#s" x="48" fill="#777"/></svg>
    <span>4,603 Reviews</span>
  </div>
  <div class="facts"><b>Departs</b> : Barcelona<br><b>Ports</b> : Barcelona Naples Rome<br><b>Dates</b> : Aug 4, Aug11, Aug 18</div>
  <p class="note">We currently have no partners with this itinerary available</p>
</article>

<div class="review-links" style="left:144px">
  <a>NORDIC AURORA <span class="circ">↓</span></a><a>ITINERARY <span class="circ">↓</span></a><a>VIEW ALL PRICES <span class="circ">↓</span></a><a>REVIEWS <span class="circ">↓</span></a>
</div>
<div class="review-links" style="left:461px">
  <a>NORDIC AURORA <span class="circ">↓</span></a><a>ITINERARY <span class="circ">↓</span></a><a>VIEW ALL PRICES <span class="circ">↓</span></a><a>REVIEWS <span class="circ">↓</span></a>
</div>

<h2 class="heading abs" style="left:114px;top:891px">Sign Up For Newsletter</h2>
<p class="subline">Get expert advice, insider tips and more.</p>
<div class="email">Enter Your E-mail</div>
<div class="send">SEND
  <svg width="14" height="13" viewBox="0 0 14 13"><path d="M0.5 6 L13.5 0.5 L10.5 12.5 L6.5 8.5 Z" fill="#fff"/><path d="M6.5 8.5 L13.5 0.5" stroke="#f15a22" stroke-width="1"/></svg>
</div>

<footer class="site-footer">
  <div class="foot-brand">GlobalPitchJourneys</div>
  <p class="copy">COPYRIGHT 2018 © GLOBALPITCHJOURNEYS<br>ALL RIGHTS RESERVED.</p>
  <span class="flag" role="img" aria-label="English language" style="left:149px;background:linear-gradient(180deg,#1f3a8a 0%,#1f3a8a 40%,#d42a35 40%,#d42a35 60%,#1f3a8a 60%)"></span>
  <span class="flag" role="img" aria-label="American English language" style="left:180px;background:repeating-linear-gradient(180deg,#c8242f 0 3px,#fff 3px 6px)"></span>
  <span class="flag" role="img" aria-label="Korean language" style="left:212px;background:#fff;border:1px solid #ddd"></span>

  <h4 class="col-title" style="left:330px">NAVIGATION</h4>
  <ul class="col-list" style="left:331px"><li>Research</li><li>Find Cruise</li><li>Write Reviews</li><li>Board</li></ul>
  <ul class="col-list" style="left:442px"><li>Login</li><li>Saved</li><li>Help</li></ul>
  <h4 class="col-title" style="left:527px">QUICK LINKS</h4>
  <ul class="col-list" style="left:528px"><li>First Time Cruisers</li><li>Find a Cruise</li></ul>
  <h4 class="col-title" style="left:670px">SOCIAL LINKS</h4>
  <ul class="col-list" style="left:671px"><li>Searchly</li><li>FaceLoop</li><li>Chirper</li><li>Pictogrid</li></ul>
</footer>
<div class="base"><span class="abs" style="left:114px;top:7px">Privacy Policy</span><span class="abs" style="left:655px;top:7px">Terms and Condition</span></div>

</body>
</html>
```